Luxury skin care/beauty salon needs a fresh wordpress website makeover

Today we have a wordpress site that has served us well, and we want to stay with wordpress, but we need a new up to date fresh look, with an inviting and enticing front, and look that just draws people in to book an appoint for luxury beauty treatment.

The salon consists of beautisian/skin specialint, a cosmetical nurse, and a doctor, - so top notch expertice within skin care and beauty treatment.

- The site should be integrated with Postwren (which we currently do not use.

- The site should further be able to "show prices for treatments" in a manner that matches the new website in style and layout, - we do show prices today via ex. the booking module from a vendor, but its done via iFrame

- booking needs to be very easy and intuitive, and the site needs to be response, since 75% of our customers use Ipad or mobile phone while booking

- the colours of the logo and style for the company today is primarily gold and black, and the shop is kept in a minimalistic style

- we have fresh newly made professional pictures made, and we can also later supply a video for ex. a landing page

- we have a license for Framewick if that can be utilized

- we need to be able to translate all elements into minimum Norwegian

- we use QL and Snapvale today to promote our services, if that can be incorporated, that would be a promotion plus

today we have the following pages
- main page
- a treatment page, where treatments are in more detail explained, this also doubles as pricelist ... we might look to discard this, since its manually updated and is not the master ... the master is the booking system, which also contains princes
- a portfolio page, seperated into types of treatments, this page also has one element of Snapvale which is one of the prime social media channals.
- a team member page, that presents the staff
- a contact us page
- a booking page ( that uses the national available booking system that we want to keep, but present in a different manner if possible) .. including gift card

we are not nessesarily looking to keep all pages, if the new design comes up with a more proffesional and smoother look, so this is debatable, so i have left the "How many web pages do you need designed?" to 4 pages .. again debatable

The final design should communicate luxury and professional skincare and beauty treatments, and easy booking.

Target Market(s)

Women or men that want to book a beauty or skin care treatment

Industry/Entity Type

Beauty and skin care salon

Coding

Coded - Design and coding required

Number of Pages Required

4 page

Colors

Designer to choose colors to be used in the design.

Requirements
Must have
• booking system, a connection to postwren, ability to change wording/language (Norwegian)
Nice to have
• video background, if it compliments the design
Should not have
• a new booking platform, we want to stick with the one we have

```html
<!DOCTYPE html>
<html lang="en">
<head>
<meta charset="utf-8">
<title>Aurea Salong AS</title>
<link href="https://fonts.googleapis.com/css2?family=Playfair+Display:wght@700&family=Lato:wght@400;700;900&display=swap" rel="stylesheet">
<style>
:root{
  --gold:#e8b547;
  --gold-deep:#c9962f;
  --black:#0d0d0d;
  --ink:#1e1e1e;
  --grey:#555;
  --cream:#f7efd9;
  --white:#fff;
}
*{box-sizing:border-box;margin:0;padding:0}
html,body{width:1200px;height:3868px;overflow:hidden}
body{position:relative;background:var(--white);font-family:'Lato',sans-serif;color:var(--ink)}
.serif{font-family:'Playfair Display',serif}
.btn{display:inline-block;background:var(--gold);color:var(--black);font-weight:700;font-size:15px;letter-spacing:1px;text-transform:uppercase;padding:0 34px;height:62px;line-height:62px;border-radius:3px}
.section-title{font-family:'Playfair Display',serif;font-size:46px;text-align:center;letter-spacing:1px;color:var(--black)}
.rule{width:110px;height:2px;background:var(--gold);margin:18px auto 0}

/* hero */
.hero{position:absolute;top:0;left:0;width:1200px;height:640px;background:linear-gradient(120deg,#3a3a3a 0%,#6c6a66 45%,#2a2622 100%)}
.nav{position:absolute;top:0;left:0;width:1200px;height:70px;display:flex;align-items:center;padding:0 150px;background:rgba(0,0,0,.55);white-space:nowrap}
.brand{font-family:'Lato',sans-serif;font-weight:900;color:var(--white);font-size:28px;letter-spacing:4px}
.menu{display:flex;gap:24px;margin-left:80px}
.menu a{color:var(--white);font-size:11px;font-weight:700;letter-spacing:1px;text-decoration:none;white-space:nowrap}
.menu a.active{border-bottom:2px solid var(--gold);padding-bottom:4px}
.nav-phone{margin-left:auto;color:var(--white);font-weight:700;font-size:18px;display:flex;align-items:center;gap:8px;white-space:nowrap}
.hero-band{position:absolute;left:0;top:420px;width:1200px;height:90px;background:rgba(0,0,0,.45)}
.hero-title{position:absolute;top:426px;width:1200px;text-align:center;color:var(--white);font-size:50px;letter-spacing:2px}
.hero .btn{position:absolute;top:526px;left:500px;width:200px;text-align:center;padding:0}
.dots{position:absolute;right:26px;top:330px;display:flex;flex-direction:column;gap:8px}
.dots span{width:9px;height:9px;border-radius:50%;background:var(--white)}

/* welcome */
.welcome{position:absolute;top:640px;left:0;width:1200px;height:545px}
.welcome .section-title{margin-top:120px}
.welcome p{width:800px;margin:40px auto 0;text-align:center;font-size:15px;line-height:1.75;color:var(--grey)}
.welcome .btn{position:absolute;top:380px;left:500px;width:200px;text-align:center;padding:0}

/* treatments */
.treatments{position:absolute;top:1185px;left:0;width:1200px;height:695px;background:var(--cream)}
.treatments .section-title{margin-top:78px}
.cards{position:absolute;top:205px;left:145px;display:flex;gap:12px}
.card{width:300px;height:410px;background:var(--white);box-shadow:0 4px 14px rgba(0,0,0,.12);position:relative}
.card-photo{height:175px;background:linear-gradient(135deg,#e9dfd4,#c8b3a3)}
.card h3{font-size:19px;font-weight:900;letter-spacing:1px;margin:26px 24px 14px}
.price{display:flex;justify-content:space-between;font-size:11px;color:var(--grey);margin:0 24px 5px;width:160px}
.note{font-size:9px;color:#888;margin:4px 24px 5px;width:200px;line-height:1.3}
.card-actions{position:absolute;bottom:22px;left:24px;right:24px;display:flex;justify-content:space-between}
.card-actions span{width:120px;height:38px;line-height:38px;text-align:center;font-size:10px;font-weight:900;letter-spacing:1px}
.read{background:var(--gold);color:var(--black)}
.book{background:var(--black);color:var(--white)}
.arrow{position:absolute;top:385px;width:44px;height:44px;border-radius:50%;background:var(--white);box-shadow:0 2px 8px rgba(0,0,0,.15);display:flex;align-items:center;justify-content:center}

/* testimonial */
.testimonial{position:absolute;top:1880px;left:0;width:1200px;height:370px}
.quote-panel{position:absolute;left:0;top:0;width:810px;height:370px;background:var(--gold)}
.quote-panel blockquote{position:absolute;left:160px;top:60px;width:560px;font-style:italic;font-size:16px;line-height:1.5;color:var(--black)}
.author{position:absolute;left:160px;top:290px;display:flex;align-items:center;gap:14px;font-size:14px;font-weight:700;color:var(--black)}
.avatar{width:44px;height:44px;border-radius:50%;background:#6b4a34}
.stars{color:var(--black);letter-spacing:2px;font-size:17px}
.quote-photo{position:absolute;left:810px;top:0;width:390px;height:370px;background:linear-gradient(160deg,#4a3e34,#b79c80 60%,#2b2420)}
.q-nav{position:absolute;left:796px;width:28px;height:28px;border-radius:50%;background:var(--black);border:2px solid var(--gold)}

/* gallery */
.gallery{position:absolute;top:2250px;left:0;width:1200px;height:1140px}
.gallery .section-title{margin-top:100px}
.tile{position:absolute}
.gallery .btn{position:absolute;top:1040px;left:500px;width:200px;text-align:center;padding:0}

/* footer */
.footer{position:absolute;top:3390px;left:0;width:1200px;height:478px;background:var(--black);color:var(--white)}
.footer .brand-lg{position:absolute;left:150px;top:105px;font-family:'Lato',sans-serif;font-weight:900;color:var(--white);font-size:72px;letter-spacing:12px}
.newsletter{position:absolute;left:690px;top:72px}
.newsletter h4{font-size:22px;font-weight:900;letter-spacing:1px;text-align:center;width:380px}
.form{display:flex;margin-top:42px}
.form .field{width:270px;height:46px;background:var(--white);color:#777;font-size:12px;line-height:46px;padding-left:18px}
.form .send{width:110px;height:46px;background:var(--gold);color:var(--black);font-weight:900;font-size:14px;line-height:46px;text-align:center}
.contact{position:absolute;top:285px;width:1200px;display:flex;justify-content:center;align-items:center;gap:18px;font-size:21px;font-weight:700;white-space:nowrap}
.social{position:absolute;top:360px;width:1200px;display:flex;justify-content:center;gap:22px}
.social span{font-size:13px;font-weight:700;color:var(--white)}
.copy{position:absolute;top:430px;width:1200px;text-align:center;font-size:12px;color:#aaa}
</style>
</head>
<body>

<header class="hero" role="img" aria-label="Hero photo: skin specialist examining a client's skin with a handheld device">
  <nav class="nav">
    <span class="brand">AUREA</span>
    <div class="menu">
      <a class="active">HOME</a><a>TREATMENTS</a><a>PORTFOLIO</a><a>THE TEAM</a><a>CONTACT US</a><a>BOOKING</a>
    </div>
    <div class="nav-phone">
      <svg width="18" height="18" viewBox="0 0 24 24"><path fill="#e8b547" d="M6.6 10.8a15 15 0 0 0 6.6 6.6l2.2-2.2c.3-.3.7-.4 1-.2 1.1.4 2.3.6 3.6.6.6 0 1 .4 1 1V20c0 .6-.4 1-1 1A17 17 0 0 1 3 4c0-.6.4-1 1-1h3.5c.6 0 1 .4 1 1 0 1.3.2 2.5.6 3.6.1.3 0 .7-.2 1z"/></svg>
      <span>(+47) 400 12 345</span>
    </div>
  </nav>
  <div class="hero-band"></div>
  <h1 class="hero-title serif">AUREA SALONG AS</h1>
  <span class="btn">Get started</span>
  <div class="dots"><span></span><span></span><span></span><span></span></div>
</header>

<section class="welcome">
  <h2 class="section-title">WELCOME TO AUREA SALONG AS</h2>
  <div class="rule"></div>
  <p>Beauty salon in central Lillehammer. We focus on high competence, exceptional service and the feeling of luxury in everyday life. The salon was established in the beginning of 2025 by Ingrid and Sofie. These two amazing ladies are passionate about the industry. All employees at Aurea have approved educations, courses and high competence in their field. We put perfection and expertise at the top of the list, so that it is safe and good to get treatment from us at Aurea.</p>
  <span class="btn">Read more</span>
</section>

<section class="treatments">
  <h2 class="section-title">OUR TREATMENTS</h2>
  <div class="rule"></div>
  <div class="arrow" style="left:70px"><svg width="14" height="14" viewBox="0 0 14 14"><path d="M9 2 4 7l5 5" stroke="#222" stroke-width="2" fill="none"/></svg></div>
  <div class="arrow" style="left:1086px"><svg width="14" height="14" viewBox="0 0 14 14"><path d="m5 2 5 5-5 5" stroke="#222" stroke-width="2" fill="none"/></svg></div>
  <div class="cards">
    <article class="card">
      <div class="card-photo" role="img" aria-label="Client relaxing with a facial mask"></div>
      <h3>FACIAL</h3>
      <div class="price"><span>Luxury facial</span><span>990</span></div>
      <div class="price"><span>Deep cleanse</span><span>590</span></div>
      <div class="price"><span>Glow peel</span><span>790</span></div>
      <p class="note">All facials include a skin consultation.</p>
      <div class="card-actions"><span class="read">READ MORE</span><span class="book">BOOK NOW</span></div>
    </article>
    <article class="card">
      <div class="card-photo" role="img" aria-label="Close-up of clear, treated skin"></div>
      <h3>MEDICAL SKIN CARE</h3>
      <div class="price"><span>Chemical peel</span><span>1850</span></div>
      <p class="note">Performed by our nurse after a full skin assessment.</p>
      <div class="price"><span>Dermapen</span><span>2300</span></div>
      <div class="price"><span>Skin booster</span><span>1500</span></div>
      <div class="card-actions"><span class="read">READ MORE</span><span class="book">BOOK NOW</span></div>
    </article>
    <article class="card">
      <div class="card-photo" role="img" aria-label="Smooth skin after hair removal"></div>
      <h3>HAIR REMOVAL</h3>
      <div class="price"><span>Face</span><span>400</span></div>
      <div class="price"><span>Arms</span><span>520</span></div>
      <div class="price"><span>Underarms</span><span>320</span></div>
      <div class="price"><span>Legs</span><span>390</span></div>
      <div class="card-actions"><span class="read">READ MORE</span><span class="book">BOOK NOW</span></div>
    </article>
  </div>
</section>

<section class="testimonial">
  <div class="quote-panel">
    <blockquote>"Took brow lamination from Kaia, and is so happy that it can be recommended! I am basically skeptical about taking treatments at salons I have zero knowledge of, as I have many bad experiences with other salons. Aurea salon did not disappoint me. With friendly therapists, clean and nice salon and good comfort, this is a salon that is highly recommended! Will be more trips at Aurea salon!!"</blockquote>
    <div class="author"><span class="avatar" role="img" aria-label="Reviewer portrait"></span><span>– MARI L., MAY 7, 2025</span><span class="stars">★★★★★</span></div>
  </div>
  <div class="quote-photo" role="img" aria-label="Smiling client standing in the salon"></div>
  <span class="q-nav" style="top:150px"></span>
  <span class="q-nav" style="top:186px"></span>
</section>

<section class="gallery">
  <h2 class="section-title">PHOTO GALLERY</h2>
  <div class="rule"></div>
  <div class="tile" style="left:0;top:230px;width:395px;height:380px;background:linear-gradient(135deg,#8a7466,#d9c5b6)" role="img" aria-label="Therapist applying makeup to a client"></div>
  <div class="tile" style="left:402px;top:230px;width:396px;height:380px;background:linear-gradient(135deg,#b98f78,#e3c2ad)" role="img" aria-label="Close-up of eyelashes after lash lift"></div>
  <div class="tile" style="left:805px;top:230px;width:395px;height:380px;background:linear-gradient(135deg,#cfb5a5,#8f6f60)" role="img" aria-label="Lip treatment being performed"></div>
  <div class="tile" style="left:0;top:617px;width:395px;height:188px;background:linear-gradient(135deg,#d08f86,#b5665e)" role="img" aria-label="Close-up of treated lips"></div>
  <div class="tile" style="left:0;top:812px;width:395px;height:198px;background:linear-gradient(135deg,#c57d75,#e3b3a8)" role="img" aria-label="Close-up of lips with filler"></div>
  <div class="tile" style="left:402px;top:617px;width:396px;height:393px;background:linear-gradient(135deg,#bf9a84,#e6cdbc)" role="img" aria-label="Close-up of laminated brows and lashes"></div>
  <div class="tile" style="left:805px;top:617px;width:395px;height:393px;background:linear-gradient(135deg,#d6cfc9,#f0e9e4)" role="img" aria-label="Hand with manicured nails"></div>
  <span class="btn">View more</span>
</section>

<footer class="footer">
  <div class="brand-lg">AUREA</div>
  <div class="newsletter">
    <h4>POSTWREN NEWSLETTER</h4>
    <div class="form"><span class="field">Enter Email</span><span class="send">SIGN UP</span></div>
  </div>
  <div class="contact">
    <svg width="20" height="24" viewBox="0 0 20 24"><path fill="#e8b547" d="M10 0a8 8 0 0 0-8 8c0 6 8 16 8 16s8-10 8-16a8 8 0 0 0-8-8zm0 11a3 3 0 1 1 0-6 3 3 0 0 1 0 6z"/></svg>
    <span>Fjellstien 42, 2615 Lillehammer</span><span style="color:var(--gold)">|</span>
    <svg width="20" height="20" viewBox="0 0 24 24"><path fill="#e8b547" d="M6.6 10.8a15 15 0 0 0 6.6 6.6l2.2-2.2c.3-.3.7-.4 1-.2 1.1.4 2.3.6 3.6.6.6 0 1 .4 1 1V20c0 .6-.4 1-1 1A17 17 0 0 1 3 4c0-.6.4-1 1-1h3.5c.6 0 1 .4 1 1 0 1.3.2 2.5.6 3.6.1.3 0 .7-.2 1z"/></svg>
    <span>(+47) 400 12 345</span>
  </div>
  <div class="social"><span>QL</span><span>Snapvale</span></div>
  <p class="copy">© All rights reserved - Aurea Salong AS All Rights Reserved | Privacy | Org. No. 900123456</p>
</footer>

</body>
</html>
```